Super elegant, crisp & clean Business card design required

We recently upgraded our branding - which is on our website - tavorelstudio.com

I would like a simple, yet elegant, clean business card design please.

The font of my logo is Cinzel - and because of the natural colour - it's best to have this on a black background.

I would like to have the back of the business card - with simply my logo.

PLEASE DO NOT SUBMIT A COMPLICATED / UNCLEAN DESIGN

Industry/Entity Type

Business

Contact Information for Business Card

Dalvik Ostrander Photography

Font styles to use
Other font styles liked:
• Cinzel

Requirements
Must have
• A backpage with nothing but my logo
• Simple design - stands out
Should not have
• Colour that dont align with my logo
• Over complicated '/ non symmetrical design

```html
<!DOCTYPE html>
<html lang="en">
<head>
<meta charset="utf-8">
<title>Dalvik Ostrander Photography — Business Card</title>
<link href="https://fonts.googleapis.com/css2?family=Cinzel:wght@400&family=Open+Sans:wght@400&display=swap" rel="stylesheet">
<style>
  :root {
    --backdrop: #e8e5df;
    --card: #fbfbfa;
    --card-shade: #ecebe8;
    --taupe: #b3aa92;
    --taupe-deep: #9d937a;
    --ink: #3c3a36;
    --ink-soft: #55524c;
  }
  * { margin: 0; padding: 0; box-sizing: border-box; }
  html, body { width: 1200px; height: 858px; overflow: hidden; background: var(--backdrop); }
  .stage { position: relative; width: 1200px; height: 858px; }

  .card {
    position: absolute; top: 279px; width: 520px; height: 300px;
    background: radial-gradient(ellipse at 55% 45%, var(--card) 55%, var(--card-shade) 100%);
    box-shadow: 0 2px 0 #dcdad5, 0 4px 0 #d2d0ca, 0 10px 24px rgba(60,50,35,.22);
    overflow: hidden;
  }
  .card--front { left: 60px; }
  .card--back { left: 620px; }

  .stripes { position: absolute; display: flex; flex-direction: column; gap: 5px; }
  .stripes span { display: block; height: 6px; background: var(--taupe); }
  .stripes--top { top: 0; left: 214px; }
  .stripes--top span { width: 70px; }
  .stripes--side { right: 0; top: 150px; align-items: flex-end; }
  .stripes--side span { width: 70px; }

  .wordmark { position: absolute; font-family: "Cinzel", serif; font-weight: 400; color: var(--taupe); text-align: center; }
  .wordmark__name { display: block; letter-spacing: .04em; }
  .wordmark__trade { display: block; letter-spacing: .55em; }
  .card--front .wordmark { top: 96px; left: 292px; width: 210px; }
  .card--front .wordmark__name { font-size: 17px; }
  .card--front .wordmark__trade { font-size: 8px; margin-top: 4px; }
  .card--back .wordmark { top: 118px; left: 0; width: 520px; }
  .card--back .wordmark__name { font-size: 30px; }
  .card--back .wordmark__trade { font-size: 11px; margin-top: 8px; }

  .holder { position: absolute; left: 0; top: 58px; display: flex; align-items: center; }
  .holder__tab { width: 26px; height: 40px; background: var(--taupe); }
  .holder__text { margin-left: 16px; font-family: "Cinzel", serif; color: var(--ink); }
  .holder__name { font-size: 19px; letter-spacing: .05em; }
  .holder__role { font-size: 11px; letter-spacing: .1em; margin-top: 2px; }

  .contacts { position: absolute; left: 42px; top: 150px; list-style: none; }
  .contacts li { display: flex; align-items: center; height: 38px; font-family: "Open Sans", sans-serif; font-size: 13px; letter-spacing: .03em; color: var(--ink-soft); }
  .contacts svg { width: 22px; height: 22px; margin-right: 14px; flex: none; }
</style>
</head>
<body>
<main class="stage">
  <section class="card card--front" aria-label="Card front">
    <div class="stripes stripes--top"><span></span><span></span><span></span></div>
    <div class="stripes stripes--side"><span></span><span></span><span></span></div>
    <div class="wordmark">
      <span class="wordmark__name">Dalvik Ostrander</span>
      <span class="wordmark__trade">Photography</span>
    </div>
    <div class="holder">
      <div class="holder__tab"></div>
      <div class="holder__text">
        <div class="holder__name">Dalvik Ostrander</div>
        <div class="holder__role">Owner</div>
      </div>
    </div>
    <ul class="contacts">
      <li>
        <svg viewBox="0 0 22 22" aria-hidden="true"><rect width="22" height="22" rx="3" fill="#9d937a"/><rect x="7" y="4" width="8" height="14" rx="1.5" fill="none" stroke="#fff" stroke-width="1.4"/><circle cx="11" cy="15.5" r="0.9" fill="#fff"/></svg>
        07946215738
      </li>
      <li>
        <svg viewBox="0 0 22 22" aria-hidden="true"><rect width="22" height="22" rx="3" fill="#9d937a"/><circle cx="11" cy="11" r="6" fill="none" stroke="#fff" stroke-width="1.3"/><path d="M5 11h12M11 5c-2.5 3-2.5 9 0 12M11 5c2.5 3 2.5 9 0 12" fill="none" stroke="#fff" stroke-width="1"/></svg>
        www.tavorelstudio.com
      </li>
      <li>
        <svg viewBox="0 0 22 22" aria-hidden="true"><rect width="22" height="22" rx="3" fill="#9d937a"/><rect x="4.5" y="6.5" width="13" height="9" rx="1" fill="none" stroke="#fff" stroke-width="1.3"/><path d="M4.5 7l6.5 5 6.5-5" fill="none" stroke="#fff" stroke-width="1.2"/></svg>
        info@tavorelstudio.com
      </li>
    </ul>
  </section>

  <section class="card card--back" aria-label="Card back">
    <div class="wordmark">
      <span class="wordmark__name">Dalvik Ostrander</span>
      <span class="wordmark__trade">Photography</span>
    </div>
  </section>
</main>
</body>
</html>
```